Flyer-Design für psychologisches Coaching  und Taiji
Flyer-Design für psychologisches Coaching und Taiji
Zielgruppe
Seit Januar 2020 habe ich mich selbständig gemacht und biete unter dem Namen 'WEGMITTE - Lene Marquardt, Coaching und Bewegung' Coaching sowie Taiji an. Der Corona-Lockdown hat meinen Geschäftseintritt stark beeinflusst, so dass ich für den Restart einen professionellen Flyer benötige, um mich und mein Angebot bekannt zu machen. Die Flyer werde ich vor meinen Räumen sowie in Geschäften im Umkreis und/oder per Einwurf verteilen.
Meine Zielgruppe sind gesundheitsorientierte Menschen in der zweiten Lebenshälfte, die ihre Balance finden wollen.
Mehr im separaten Dokument, bitte lesen.
Aufgabenstellung
Das Design soll zum Logo und zu meinem angestrebten Image passen. Ich möchte seriös, sympathisch und authentisch rüberkommen. Das psychologische Coaching und Taiji sollen gleichwertig und harmonisch präsentiert werden. Die Texte sollen kurz und prägnant sein. Textvorschläge gebe ich im Briefing und freue mich über neue, aussagefähige Formulierungen.
Mehr im beigefügten Dokument, bitte lesen.

```html
<!DOCTYPE html>
<html lang="de">
<head>
<meta charset="utf-8">
<title>WEGMITTE – Flyer</title>
<link href="https://fonts.googleapis.com/css2?family=Cinzel:wght@500;600&family=Quicksand:wght@400;500;600;700&display=swap" rel="stylesheet">
<style>
  :root{
    --olive:#a9a24c;
    --blue-top:#1f5fae;
    --blue-mid:#4f8fd0;
    --sunset:#f08a3a;
    --ground:#5a4637;
    --ink:#4d4d4d;
    --paper:#ffffff;
    --panel-grey:#ececec;
    --bg:#eef0f1;
  }
  *{box-sizing:border-box;margin:0;padding:0}
  html,body{width:1200px;height:1200px;overflow:hidden;background:var(--bg)}
  body{position:relative;font-family:"Quicksand",sans-serif;color:var(--ink)}
  .spread{position:absolute;left:160px;width:880px;height:560px;display:flex;background:var(--paper);box-shadow:0 10px 30px rgba(0,0,0,.12)}
  .spread--outside{top:30px}
  .spread--inside{top:610px}
  .panel{position:relative;width:293.33px;height:100%;overflow:hidden;padding:24px 22px}
  .panel + .panel{border-left:1px solid #e4e4e4}
  .band{position:absolute;left:0;right:0;bottom:0;height:78px;background:var(--olive)}
  .band-line{position:absolute;left:0;right:0;height:2px;background:rgba(255,255,255,.55)}
  h2{font-weight:600;font-size:11px;letter-spacing:.12em;color:var(--olive);text-transform:uppercase;margin-bottom:10px}
  h3{font-weight:500;font-size:8.6px;letter-spacing:.04em;color:var(--olive);margin:12px 0 5px}
  p,li{font-size:7.1px;line-height:1.5}
  p + p{margin-top:3px}
  ul{list-style:none}
  li::before{content:"• "}
  b{font-weight:700;color:#3c3c3c}
  .photo{position:absolute;border:4px solid var(--paper);box-shadow:0 1px 4px rgba(0,0,0,.15)}
  .photo--meditation{left:110px;top:370px;width:118px;height:178px;background:linear-gradient(160deg,#7a9a7e,#c9a9a0 45%,#2c2c2c 80%)}
  .photo--room{left:14px;top:410px;width:262px;height:140px;background:linear-gradient(180deg,#f4f2ee 0%,#b4a7bc 30%,#d7cdbd 58%,#b98352 100%)}
  .photo--portrait{left:70px;top:398px;width:166px;height:108px;border:none;background:linear-gradient(135deg,#7a1b1f,#a43a36 60%,#d8c2b6)}
  .photo--taiji{left:30px;top:368px;width:128px;height:182px;background:linear-gradient(160deg,#c9b8c7,#7f9c7e 45%,#2a2a2a 75%,#c2a074)}
  /* brand name: text font, one colour, one weight, plain square beside it */
  .brand{display:flex;align-items:center;justify-content:center;gap:8px}
  .brand-mark{width:10px;height:10px;background:var(--olive)}
  .brand-name{font-family:"Quicksand",sans-serif;font-weight:700;font-size:17px;color:var(--olive);letter-spacing:.12em}
  .contact-card{position:absolute;left:14px;top:0;width:265px;height:200px;background:#f7f7f7;padding:52px 0 0}
  .contact{margin:34px 0 0 36px;font-size:7.4px;letter-spacing:.18em;line-height:2.25;color:var(--olive);font-weight:600;list-style:none}
  .contact li::before{content:none}
  .rooms{position:absolute;left:14px;right:14px;top:228px}
  /* cover */
  .cover{padding:0;background:linear-gradient(180deg,var(--blue-top) 0%,var(--blue-mid) 32%,#9cc2de 48%,#f6c27a 60%,var(--sunset) 70%,#7b5a4a 82%,var(--ground) 100%)}
  .cover-logo{position:absolute;left:58px;top:0;width:92px;height:90px;background:rgba(230,230,230,.95);display:flex;align-items:center;justify-content:center}
  .cover-logo .brand{gap:5px}
  .cover-logo .brand-mark{width:6px;height:6px}
  .cover-logo .brand-name{font-size:10.5px;letter-spacing:.08em}
  .cover-tag{position:absolute;top:116px;left:0;right:0;text-align:center;color:#fff;font-size:6.6px;font-weight:700;letter-spacing:.32em;line-height:1.9;text-transform:uppercase}
  .cover-title{position:absolute;top:150px;left:0;right:0;text-align:center;font-family:"Cinzel",serif;font-weight:500;color:#fff;font-size:19px;line-height:1.18;letter-spacing:.02em}
  .cover-scene{position:absolute;left:0;right:0;top:200px;bottom:60px}
  .cover .band{height:60px;display:flex;align-items:center;justify-content:center}
  .cover-band-text{color:#fff;font-size:6.6px;font-weight:700;letter-spacing:.28em;text-transform:uppercase}
  /* inside intro */
  .intro{background:linear-gradient(180deg,#f5f5f5,var(--panel-grey));text-align:center;padding:0 18px}
  .intro-text{position:absolute;left:18px;right:18px;top:178px;text-align:left}
  .offers{position:absolute;left:18px;right:18px;top:258px}
  .offers-lead{font-size:8.4px;color:var(--olive);font-weight:500;line-height:1.4;margin-bottom:14px}
  .offer-title{font-size:10px;font-weight:600;letter-spacing:.14em;color:var(--olive);text-transform:uppercase;margin-top:12px}
  .offer-text{font-size:7px;margin-top:3px}
</style>
</head>
<body>

<section class="spread spread--outside" aria-label="Flyer Außenseite">
  <article class="panel">
    <h2>Meditation</h2>
    <p>Kennen Sie das? Sie haben noch 1000 Dinge auf Ihrer to-do-Liste und wissen nicht, wo Ihnen der Kopf steht. Außerdem haben Sie gerade eine schwierige Phase in der Firma. Und schon länger diesen Stress in Ihrer Familie. Und Sie wissen, dass Sie endlich mal was für sich tun sollten. Aber wann denn bloß?</p>
    <p>Für mehr und mehr Menschen ist es wichtig geworden, im hektischen Alltag Inseln der Ruhe zu schaffen.</p>
    <h3>Offene Meditationsabende</h3>
    <p>Falls Sie es ausprobieren möchten oder eine regelmäßige Meditationsgruppe suchen, kommen Sie doch einfach zu einem meiner offenen Meditationsabende. Jede/r ist herzlich eingeladen, unabhängig von der Vorerfahrung mit Meditation.</p>
    <p>Wir erkunden unter meiner Anleitung verschiedenen Techniken aus verschiedenen Meditationspraktiken frei von religiöser oder spiritueller Bindung.</p>
    <p>Diese Abende biete ich auf der Basis freiwilliger Kostenbeteiligung an. Die Termine finden Sie auf dem Terminblatt oder auf meiner Website.</p>
    <div class="band"><span class="band-line" style="top:26px"></span><span class="band-line" style="top:50px"></span></div>
    <div class="photo photo--meditation" role="img" aria-label="Foto: Kursleiterin sitzt meditierend vor einem Wandbild, davor eine Kerze"></div>
  </article>

  <article class="panel">
    <div class="contact-card">
      <div class="brand">
        <span class="brand-mark"></span>
        <span class="brand-name">WEGMITTE</span>
      </div>
      <ul class="contact">
        <li>Ahornstraße 22</li>
        <li>61352 Lindenau</li>
        <li>www.wegmitte-coaching.de</li>
        <li>info@wegmitte-coaching.de</li>
        <li>Mobil: 0160 4427915</li>
      </ul>
    </div>
    <div class="rooms">
      <p>Die Räumlichkeiten befinden sich in der Innenstadt Lindenaus. Auf der Grundfläche von ca. 75 m² finden die Kurse und Coachings statt.</p>
      <p style="margin-top:8px">Parkmöglichkeiten: Fußläufig ist das Parkhaus am Marktplatz zu erreichen.</p>
    </div>
    <div class="band"><span class="band-line" style="top:30px"></span><span class="band-line" style="top:54px"></span></div>
    <div class="photo photo--room" role="img" aria-label="Foto: heller Kursraum mit Holzboden, Meditationskissen und farbigem Wandbild"></div>
  </article>

  <article class="panel cover">
    <div class="cover-logo">
      <div class="brand">
        <span class="brand-mark"></span>
        <span class="brand-name">WEGMITTE</span>
      </div>
    </div>
    <p class="cover-tag">Zur Ruhe kommen und<br>zu sich selbst finden mit</p>
    <h1 class="cover-title">TAI CHI, QIGONG,<br>MEDITATION</h1>
    <div class="cover-scene" role="img" aria-label="Foto: Person mit ausgebreiteten Armen auf einem Berggipfel im Sonnenaufgang"></div>
    <div class="band"><span class="cover-band-text">Gruppenkurse und Einzelunterricht</span></div>
  </article>
</section>

<section class="spread spread--inside" aria-label="Flyer Innenseite">
  <article class="panel intro">
    <p class="intro-text">Die Angebote von „WEGMITTE – Lene Marquardt“ helfen Ihnen dabei, <b>sich neu auszurichten, zur Ruhe zu kommen und zu sich selbst zu finden.</b> Dabei lege ich Wert auf die Verbindung von <b>Geist, Körper und Seele</b> und setze dafür gezielt körperorientierte Methoden und die Lenkung der Aufmerksamkeit (des inneren Fokus) ein.</p>
    <div class="offers">
      <p class="offers-lead">Bei mir finden Sie Coaching und Bewegung,<br>im Einzelnen heißt das:</p>
      <p class="offer-title">Psychologisches Coaching</p>
      <p class="offer-text">ich begleite Sie in schwierigen Lebensphasen mit körperorientierten Methoden</p>
      <p class="offer-title">Taiji und Qigong</p>
      <p class="offer-text">erleben Sie sich mit langsamen Bewegungen im Fluss</p>
      <p class="offer-title">Meditation</p>
      <p class="offer-text">richten Sie den Fokus ganz nach innen und…<br>einfach nur sein</p>
    </div>
    <div class="band"><span class="band-line" style="top:26px"></span><span class="band-line" style="top:50px"></span></div>
  </article>

  <article class="panel">
    <h2>Psychologisches Coaching</h2>
    <p>Wünschen Sie sich <b>Begleitung</b> in Situationen, die Sie selbst als schwierig empfinden? Ich biete Ihnen:</p>
    <ul style="margin-top:6px">
      <li><b>Hilfe zur Selbsthilfe</b>, z.B. in persönlichen Krisensituationen (Trennung, Konflikte, Ängste)</li>
      <li><b>Neuorientierung</b>, beruflich und privat, unter Berücksichtigung Ihrer individuellen Stärken und Bedürfnisse</li>
      <li>Methoden und Ansätze zur <b>Stressbewältigung</b>, um sich vor Erschöpfung und Burn-out zu schützen</li>
      <li>Meine eigene <b>Lebens- und Berufserfahrung</b> als Führungskraft mit zahlreichen einschneidenden Veränderungen sowie einen umfangreichen <b>Methoden-Fundus</b></li>
    </ul>
    <h3>Ihr nachhaltiger Nutzen:</h3>
    <ul>
      <li>verbesserte <b>Stress und Belastungsresistenz</b></li>
      <li><b>veränderte Einstellung</b>, die Ihnen mehr Spielraum gibt</li>
      <li><b>neue Möglichkeiten</b>, schwierige Situationen zu meistern</li>
      <li><b>Sie sehen klarer</b>, wer Sie sind und was Sie wollen</li>
    </ul>
    <h3>Gerne bin ich für Sie da.</h3>
    <p>Vereinbaren Sie unverbindlich ein kostenloses Erstgespräch mit mir entweder per Mail unter <b>info@wegmitte-coaching.de</b> oder telefonisch unter <b>0160 4427915</b>.</p>
    <div class="band"><span class="band-line" style="top:26px"></span><span class="band-line" style="top:50px"></span></div>
    <div class="photo photo--portrait" role="img" aria-label="Porträtfoto der Coachin vor dunkelrotem Hintergrund"></div>
  </article>

  <article class="panel">
    <h2>Taiji und Qigong</h2>
    <p>Taiji und Qigong sind langsame und fließende Bewegungen. Beides stammt aus den Kampfkünsten im alten China und dient der Gesundheitsförderung. Ich unterrichte nach der Tradition der Familie Chen. Die Teilnehmenden richten Ihre Aufmerksamkeit nach innen bzw. ganz auf die Bewegungen. Der meditative Aspekt steht für mich klar im Vordergrund.</p>
    <h3>Möglicher Nutzen für Sie:</h3>
    <ul>
      <li>Mehr Ruhe und Gelassenheit im Alltag</li>
      <li>Schulung der Konzentration</li>
      <li>Verbesserung der Körperwahrnehmung</li>
      <li>Kräftigung der Sehnen und Gelenke</li>
      <li>Aufrechtere Körperhaltung</li>
    </ul>
    <h3>Wie können Sie einsteigen?</h3>
    <p>Bitte besuchen Sie immer zuerst eine <b>kostenlose Schnupperstunde</b> bei mir, um Taiji und Qigong einfach mal auszuprobieren. Wann die nächsten Schnupperstunden stattfinden, sehen sie auf dem Terminblatt oder auf meiner Website.</p>
    <div class="band"><span class="band-line" style="top:26px"></span><span class="band-line" style="top:50px"></span></div>
    <div class="photo photo--taiji" role="img" aria-label="Foto: Kursleiterin in Taiji-Haltung mit erhobenen Armen vor einem Wandbild"></div>
  </article>
</section>

</body>
</html>
```